Business Card for TQB Field Services

Would like a large logo on one side. On the other side, logo on one side and company phone number, address, and email on the other side. I don't have a logo so please create one for us.
Updates
I don't have a logo, so please create one for us.
Target Market(s)
Land Surveying
Industry/Entity Type
Surveyor
Contact Information for Business Card
Would like a large logo on one side. On the other side, logo on one side and company phone number, address, and email on the other side
Requirements
Nice to have
- would like the initials to be incorporated with the logo

```html
<!DOCTYPE html>
<html lang="en">
<head>
<meta charset="UTF-8">
<title>TQB Field Services – Business Card</title>
<link href="https://fonts.googleapis.com/css2?family=Open+Sans:wght@400;600&family=Archivo+Narrow:wght@700&display=swap" rel="stylesheet">
<style>
  :root {
    --backdrop: #ebe7e1;
    --kraft: #c3a67b;
    --kraft-light: #cbb088;
    --ink: #151210;
    --rule: #5a4a35;
  }
  * { box-sizing: border-box; margin: 0; padding: 0; }
  html, body {
    width: 1200px;
    height: 900px;
    overflow: hidden;
    background: var(--backdrop);
  }
  .canvas {
    position: relative;
    width: 1200px;
    height: 900px;
  }
  .card {
    position: absolute;
    width: 556px;
    height: 342px;
    background: linear-gradient(160deg, var(--kraft-light), var(--kraft));
    color: var(--ink);
    box-shadow: 0 6px 18px rgba(0,0,0,0.18);
  }
  .card--front { left: 238px; top: 62px; }
  .card--back  { left: 459px; top: 518px; }

  .contact-block {
    position: absolute;
    left: 0;
    right: 0;
    top: 114px;
    text-align: center;
    font-family: "Open Sans", sans-serif;
  }
  .contact-block__name {
    font-weight: 600;
    font-size: 18px;
    line-height: 24px;
  }
  .contact-block__title {
    font-weight: 400;
    font-size: 14px;
    line-height: 18px;
  }
  .contact-block__rule {
    width: 108px;
    height: 1px;
    margin: 14px auto 10px;
    background: var(--rule);
  }
  .contact-block__line {
    font-size: 14px;
    line-height: 20px;
  }

  .brand {
    position: absolute;
    left: 0;
    right: 0;
    top: 0;
    bottom: 0;
    display: flex;
    flex-direction: column;
    align-items: center;
    justify-content: center;
    gap: 22px;
  }
  .brand__square {
    width: 120px;
    height: 120px;
    background: var(--ink);
  }
  .brand__name {
    font-family: "Archivo Narrow", sans-serif;
    font-weight: 700;
    font-size: 32px;
    line-height: 1;
    color: var(--ink);
  }
</style>
</head>
<body>
  <main class="canvas">
    <section class="card card--front">
      <div class="contact-block">
        <p class="contact-block__name">Daniel Harper</p>
        <p class="contact-block__title">Managing Director</p>
        <div class="contact-block__rule"></div>
        <p class="contact-block__line">044-987 654 321</p>
        <p class="contact-block__line">hello@tqbfield.com</p>
        <p class="contact-block__line">www.tqbfield.com</p>
      </div>
    </section>

    <section class="card card--back">
      <div class="brand">
        <div class="brand__square"></div>
        <p class="brand__name">TQB Field Services</p>
      </div>
    </section>
  </main>
</body>
</html>
```